Design the New 3D Printing Database - MeshLocker.net

We’re hiring a designer to create a modern, intuitive, and scalable frontend design for MeshLocker.net — a search engine and aggregator for free 3D printable files (STL files).

The site will not host files, but will crawl and display listings from other 3D file platforms like Plankora, Buildwisp, and OurTinyForgeworks. We need a design that looks clean, tech-forward, and makes it easy for users to browse, search, and explore curated 3D print models.

Project Goals
• Help users search, filter, and browse STL files from various sources
• Present file listings in a clean and organized card-style layout
• Include strong category navigation, tag filtering, and search UX
• Allow for expansion — community features, user accounts, ads, etc.
• Be ready for handoff to developers

Pages & Components to Design

1. Homepage
• Featured models / Trending prints
• Search bar with predictive text
• Top categories (e.g., Tools, Toys, Miniatures, Cosplay)
• Optional: promo ad slot or “Featured Site of the Week”

2. Search Results Page
• Search bar at top
• Grid or list view of STL listings
• Filters on sidebar (category, tag, source site, popularity)
• Sort options (Newest, Most Viewed, Top Rated)

3. Individual File Listing Page
• Model thumbnail (placeholder for external image)
• Title, description, tags
• Source website badge/logo
• Button: “View on [Source Site]”
• Optional: 3D viewer embed (room for iframe or canvas)

4. Category Pages
• Header with category name and short description
• Grid of listings in that category

5. About / FAQ / Submit a File
• Basic static content page layout
• Contact form or submission form mockup

6. Admin Preview (Optional)
• Just 1-2 styled screens for how backend editing might look (not functional)

Design Requirements
• Responsive (desktop, tablet, mobile)
• Clean, modern UI (think: Web3 simplicity, Zentavo-level UX)
• Easy-to-read typography and smart use of whitespace
• Icons or badges for source platforms (e.g., Plankora, Buildwisp)
• Room for advertising placements (sidebar, inline, or homepage)

Style Inspiration
• Hero inspiration: FabScoutly.net — but cleaner
• Other ideas: Quillo Commons, Brivvells
• Optional: light/dark mode theme toggle

Deliverables
• Complete desktop and mobile Figma designs
• Style guide (colors, fonts, components)
• Assets and UI kit for development handoff
• Optionally, clickable prototype for demonstration

Target Market(s)

3D Printing Enthusiasts

Industry/Entity Type

3D Printing, Design, Engineering

Number of Pages Required

5+ page

Font styles to use
Sans Serif

```html
<!DOCTYPE html>
<html lang="en">
<head>
<meta charset="utf-8">
<title>MeshLocker.net — Fresh Finds for Your Next Printing</title>
<link href="https://fonts.googleapis.com/css2?family=Urbanist:wght@500;600;700&family=Poppins:wght@400;500;600;700&display=swap" rel="stylesheet">
<style>
:root{
  --orange:#F0962A;
  --pink:#E8127C;
  --yellow:#FFF200;
  --blue:#1C8ED6;
  --ink:#0B0B0B;
  --text:#1E1E1E;
  --muted:#7A7A7A;
  --line:#E6E6E6;
  --card:#FFFFFF;
  --soft:#F6F6F6;
}
*{box-sizing:border-box;margin:0;padding:0}
html,body{width:1200px;height:3530px;overflow:hidden}
body{position:relative;background:#fff;font-family:'Poppins',sans-serif;color:var(--text)}
.abs{position:absolute}
.display{font-family:'Urbanist',sans-serif;font-weight:600;letter-spacing:-0.5px}

.topbar{left:0;top:0;width:1200px;height:38px;background:var(--ink);color:#fff;font-size:11px;font-weight:600}
.topbar .promo{position:absolute;left:0;right:0;top:12px;text-align:center}
.topbar .promo span{color:var(--orange)}
.theme{position:absolute;right:90px;top:9px;display:flex;align-items:center;gap:10px;font-size:10px}
.toggle{width:46px;height:22px;border-radius:11px;background:#fff;position:relative}
.toggle::before{content:"";position:absolute;left:2px;top:2px;width:18px;height:18px;border-radius:50%;background:var(--orange)}

.header{left:0;top:38px;width:1200px;height:102px;border-bottom:1px solid var(--line)}
.logo{font-family:'Urbanist',sans-serif;font-weight:600;font-size:38px;color:var(--ink);letter-spacing:-1px}
.header .logo{left:89px;top:26px}
.search{left:429px;top:30px;width:366px;height:40px;border-radius:20px;background:var(--soft);border:1px solid #ececec;font-size:12px;color:var(--muted)}
.search .kw{position:absolute;left:16px;top:11px}
.search .sep{position:absolute;left:196px;top:9px;width:1px;height:22px;background:#cfcfcf}
.search .cat{position:absolute;left:209px;top:11px}
.search .go{position:absolute;right:4px;top:4px;width:32px;height:32px;border-radius:50%;background:#fff;display:flex;align-items:center;justify-content:center}
.btn{display:inline-flex;align-items:center;justify-content:center;border-radius:22px;background:var(--orange);color:#fff;font-weight:700;font-size:13px;letter-spacing:.3px}
.specials{left:831px;top:29px;width:128px;height:42px}
.hicons{left:992px;top:36px;display:flex;gap:16px;align-items:center}
.cart{position:relative}
.cart b{position:absolute;right:-6px;top:-6px;width:14px;height:14px;border-radius:50%;background:var(--orange);color:#fff;font-size:9px;display:flex;align-items:center;justify-content:center}

.nav{left:0;top:140px;width:1200px;height:61px;display:flex;justify-content:center;align-items:center;gap:60px;font-size:13px;color:#333}

.hero-copy{left:0;top:201px;width:544px;height:670px;background:linear-gradient(180deg,#f6f6f6 0%,#e2e2e2 100%)}
.hero-photo{left:544px;top:201px;width:656px;height:670px;background:radial-gradient(circle at 55% 60%,#2e6ea8 0%,#1f4a74 35%,#2c2a2a 70%,#141414 100%)}
.welcome{left:89px;top:352px;font-size:28px;font-weight:500}
.hero-title{left:89px;top:392px;font-size:68px;line-height:62px;color:var(--ink)}
.hero-title em{font-style:normal;color:var(--pink)}
.explore{left:89px;top:608px;width:199px;height:42px}
.dots{left:89px;top:809px;display:flex;gap:7px;align-items:center}
.dots i{width:7px;height:7px;border-radius:50%;background:#b5b5b5}
.dots i.on{width:64px;height:6px;border-radius:3px;background:var(--ink)}

.section-title{left:0;width:1200px;text-align:center;font-size:42px;color:var(--ink)}
.cat-row{left:0;top:1025px;width:1200px}
.cat{position:absolute;width:160px;margin-left:-80px;text-align:center}
.ring{width:124px;height:124px;border-radius:50%;margin:0 auto;border:4px solid;padding:3px;background:#fff}
.ring div{width:100%;height:100%;border-radius:50%}
.cat p{font-family:'Urbanist',sans-serif;font-weight:600;font-size:23px;margin-top:10px;color:var(--ink)}
.arrows{left:546px;top:1213px;display:flex;gap:10px}
.arrows span{width:50px;height:50px;border-radius:50%;display:flex;align-items:center;justify-content:center}

.trend-photo{left:89px;top:1352px;width:504px;height:388px;border-radius:16px;background:linear-gradient(135deg,#e9e9ea 0%,#cfd2d3 45%,#b98a6d 70%,#d7d35b 100%)}
.trend-card{left:607px;top:1352px;width:503px;height:388px;border-radius:16px;background:var(--orange);color:#fff;padding:44px 40px}
.trend-card h2{font-size:42px;font-weight:600}
.trend-card .lead{font-size:13px;margin-top:8px;line-height:19px;width:380px}
.trend-card ul{margin-top:16px;list-style:none;font-family:'Urbanist',sans-serif;font-weight:600;font-size:17px}
.trend-card li{margin-bottom:10px;padding-left:20px;position:relative}
.trend-card li::before{content:"";position:absolute;left:1px;top:8px;width:7px;height:7px;border-radius:50%;background:#fff}
.trend-card .view{position:absolute;left:28px;top:296px;width:199px;height:42px;background:#fff;color:var(--ink);font-size:13px}

.subtitle{left:0;top:1874px;width:1200px;text-align:center;font-size:13px;color:#666}
.cards{left:89px;top:1926px;display:flex;gap:15px}
.card{width:244px;height:282px;background:var(--card);border-radius:14px;box-shadow:0 6px 24px rgba(0,0,0,.07);position:relative}
.card .thumb{height:132px;display:flex;align-items:center;justify-content:center;border-bottom:1px solid var(--line);margin:0 8px}
.card .thumb div{width:150px;height:90px;border-radius:10px}
.card h3{font-family:'Urbanist',sans-serif;font-weight:600;font-size:17px;margin:20px 16px 0;white-space:nowrap;overflow:hidden;text-overflow:ellipsis}
.card .crumb{font-size:11px;color:var(--muted);margin:6px 16px 0}
.card .meta{position:absolute;left:8px;right:8px;top:220px;border-top:1px solid var(--line);padding:16px 8px 0;display:flex;gap:26px;font-size:11px;color:var(--muted)}
.card .meta span{display:flex;align-items:center;gap:8px}

.share{left:89px;top:2344px;width:1022px;height:238px;border-radius:20px;background:var(--ink);overflow:hidden}
.share-deco{position:absolute;right:0;top:0;width:440px;height:238px;background:linear-gradient(120deg,rgba(255,242,0,0) 0%,rgba(255,242,0,.55) 45%,rgba(232,18,124,.7) 100%)}
.share-person{left:760px;top:2267px;width:180px;height:315px;border-radius:90px 90px 0 0;background:linear-gradient(180deg,#8b9299 0%,#c7b08a 45%,#e6cdb1 75%,#7c8a95 100%)}
.share-title{left:141px;top:2383px;font-size:40px;color:#fff}
.share-text{left:142px;top:2436px;width:560px;font-size:13px;line-height:19px;color:#fff}
.share-btn{left:144px;top:2491px;width:198px;height:42px;gap:8px}

.steps{left:188px;top:2737px;display:flex;gap:15px}
.step{width:265px;height:250px;border-radius:14px;background:#fff;box-shadow:0 6px 24px rgba(0,0,0,.07);text-align:center;padding-top:26px}
.num{width:94px;height:94px;border-radius:50%;background:var(--ink);border:4px solid;margin:0 auto;color:#fff;font-family:'Urbanist',sans-serif;font-weight:600;font-size:40px;display:flex;align-items:center;justify-content:center}
.step h3{font-family:'Urbanist',sans-serif;font-weight:600;font-size:23px;margin-top:16px;color:var(--ink)}
.step p{font-size:13px;line-height:19px;color:#7d7d7d;margin:8px auto 0;width:205px}

.footer{left:0;top:3085px;width:1200px;height:445px;background:var(--ink);color:#fff}
.footer .logo{position:absolute;left:89px;top:150px;color:#fff}
.social{position:absolute;left:142px;top:199px;display:flex;gap:12px}
.social i{width:40px;height:40px;border-radius:50%;border:1.5px solid #fff;display:flex;align-items:center;justify-content:center}
.social i::after{content:"";width:12px;height:12px;border-radius:50%;background:#fff}
.fcol{position:absolute;top:84px}
.fcol h4{font-family:'Urbanist',sans-serif;font-weight:600;font-size:19px}
.fcol ul{list-style:none;margin-top:14px;font-size:12px;color:#cfcfcf}
.fcol li{height:27px}
.email{position:absolute;left:788px;top:125px;width:322px;height:49px;border-radius:25px;border:1px solid #3a3a3a;background:#121212;font-size:12px;color:#aaa;display:flex;align-items:center;gap:10px;padding-left:24px}
.subscribe{position:absolute;left:788px;top:187px;width:322px;height:46px;justify-content:center}
.subscribe svg{position:absolute;right:20px}
.divider{position:absolute;left:89px;top:370px;width:1022px;height:1px;background:#333}
.copy{position:absolute;left:0;top:397px;width:1200px;text-align:center;font-size:14px;letter-spacing:-0.3px;font-family:'Urbanist',sans-serif;font-weight:600}
.chat{position:absolute;left:1134px;top:355px}
</style>
</head>
<body>

<div class="abs topbar">
  <div class="promo">FREE SHIPPING ON QUALIFYING ORDERS* <span>SEE DETAILS</span></div>
  <div class="theme">LITE <span class="toggle"></span> DARK</div>
</div>

<header class="abs header">
  <div class="abs logo">Logo Here</div>
  <div class="abs search">
    <span class="kw">Search by keyword</span><span class="sep"></span><span class="cat">Categories</span>
    <span class="go"><svg width="14" height="14" viewBox="0 0 24 24" fill="none" stroke="#555" stroke-width="2.4"><circle cx="11" cy="11" r="7"/><path d="M16 16l5 5"/></svg></span>
  </div>
  <div class="abs btn specials">SPECIALS</div>
  <div class="abs hicons">
    <svg width="28" height="24" viewBox="0 0 28 24" stroke="#111" stroke-width="2.4" stroke-linecap="round"><path d="M4 4h20M8 12h16M4 20h20"/></svg>
    <svg width="26" height="26" viewBox="0 0 24 24" fill="none" stroke="#111" stroke-width="2"><circle cx="12" cy="8" r="4.5"/><path d="M3.5 22c1-5 4.5-7 8.5-7s7.5 2 8.5 7"/></svg>
    <span class="cart"><svg width="28" height="26" viewBox="0 0 24 24" fill="none" stroke="#111" stroke-width="2" stroke-linejoin="round"><path d="M1 3h3l3 12h12l3-9H6"/><circle cx="9" cy="20" r="1.6"/><circle cx="18" cy="20" r="1.6"/></svg><b>0</b></span>
  </div>
</header>

<nav class="abs nav">
  <span>HOME</span><span>CATEGORIES</span><span>POPULAR</span><span>SUBMIT A FILE</span><span>ABOUT US</span><span>FAQ</span><span>CONTACT US</span>
</nav>

<section>
  <div class="abs hero-copy"></div>
  <div class="abs hero-photo" role="img" aria-label="Close-up of a 3D printer nozzle printing an intricate blue lattice model under warm orange light"></div>
  <div class="abs welcome display">Welcome To</div>
  <h1 class="abs hero-title display">Fresh Finds<br>for Your <em>Next</em><br>Printing</h1>
  <div class="abs btn explore">EXPLORE STL FILES</div>
  <div class="abs dots"><i></i><i></i><i class="on"></i><i></i><i></i></div>
</section>

<section>
  <h2 class="abs section-title display" style="top:948px">Explore by Category</h2>
  <div class="abs cat-row">
    <div class="cat" style="left:175px"><div class="ring" style="border-color:var(--pink)"><div role="img" aria-label="Teddy bear and colourful toys" style="background:linear-gradient(135deg,#c98a55,#e14b3b 60%,#f4d04a)"></div></div><p>Toys</p></div>
    <div class="cat" style="left:344px"><div class="ring" style="border-color:var(--orange)"><div role="img" aria-label="Miniature town diorama" style="background:linear-gradient(135deg,#6f7d88,#a38b6e 60%,#3f4a52)"></div></div><p>Miniatures</p></div>
    <div class="cat" style="left:516px"><div class="ring" style="border-color:var(--blue)"><div role="img" aria-label="Hands holding hand tools" style="background:linear-gradient(135deg,#2c3340,#c99a7c 55%,#d8b531)"></div></div><p>Tools</p></div>
    <div class="cat" style="left:684px"><div class="ring" style="border-color:var(--pink)"><div role="img" aria-label="Cosplay costume at a convention" style="background:linear-gradient(135deg,#58606c,#d69b4a 55%,#c46a3a)"></div></div><p>Cosplay</p></div>
    <div class="cat" style="left:856px"><div class="ring" style="border-color:var(--orange)"><div role="img" aria-label="Golden leaf art piece" style="background:linear-gradient(135deg,#2a2416,#b88a2c 55%,#5a3d6a)"></div></div><p>Art</p></div>
    <div class="cat" style="left:1025px"><div class="ring" style="border-color:var(--blue)"><div role="img" aria-label="Fantasy sunset landscape" style="background:linear-gradient(180deg,#f0a23a,#c4431c 55%,#2a1a14)"></div></div><p>Fantasy</p></div>
  </div>
  <div class="abs arrows">
    <span style="background:var(--ink)"><svg width="12" height="12" viewBox="0 0 12 12" fill="none" stroke="#fff" stroke-width="2"><path d="M8 2L4 6l4 4"/></svg></span>
    <span style="background:var(--orange)"><svg width="12" height="12" viewBox="0 0 12 12" fill="none" stroke="#fff" stroke-width="2"><path d="M4 2l4 4-4 4"/></svg></span>
  </div>
</section>

<section>
  <div class="abs trend-photo" role="img" aria-label="Two makers reviewing a laptop next to a desktop 3D printer"></div>
  <div class="abs trend-card">
    <h2 class="display">Trending 3D Models</h2>
    <p class="lead">Updated daily — check out what's hot in the 3D printing community.</p>
    <ul><li>Thumbnail Image</li><li>Title</li><li>Tags</li><li>Source badge (e.g., Plankora)</li></ul>
    <div class="btn view">VIEW ON SOURCE</div>
  </div>
</section>

<section>
  <h2 class="abs section-title display" style="top:1815px">Featured Source Platform</h2>
  <p class="abs subtitle">This week we're highlighting [Buildwisp], a go-to platform for high-quality STL files.</p>
  <div class="abs cards">
    <article class="card"><div class="thumb"><div role="img" aria-label="Steel pot with wooden lid holder" style="background:radial-gradient(circle,#d9d9d9,#b08a55 70%,#fff 72%)"></div></div><h3>Pot Lid Holder 12cm...</h3><p class="crumb">Household &nbsp;›&nbsp; Kitchen</p>
      <div class="meta"><span><svg width="20" height="18" viewBox="0 0 24 22" fill="none" stroke="#222" stroke-width="1.8"><path d="M12 20S2 14 2 7.5A5 5 0 0112 5a5 5 0 0110 2.5C22 14 12 20 12 20z"/></svg>3,097</span><span><svg width="20" height="20" viewBox="0 0 24 24" fill="none" stroke="#222" stroke-width="1.8" stroke-linejoin="round"><path d="M12 2l3 6.5 7 .8-5.2 4.8 1.5 7L12 17.6 5.7 21l1.5-7L2 9.3l7-.8z"/></svg>5</span></div></article>
    <article class="card"><div class="thumb"><div role="img" aria-label="Orange model sports car" style="background:radial-gradient(ellipse,#f0a21e,#d9731b 60%,#fff 72%)"></div></div><h3>Vantor 130 RS 1:24 color...</h3><p class="crumb">Makers &nbsp;›&nbsp; Automotive</p>
      <div class="meta"><span><svg width="20" height="18" viewBox="0 0 24 22" fill="none" stroke="#222" stroke-width="1.8"><path d="M12 20S2 14 2 7.5A5 5 0 0112 5a5 5 0 0110 2.5C22 14 12 20 12 20z"/></svg>3,097</span><span><svg width="20" height="20" viewBox="0 0 24 24" fill="none" stroke="#222" stroke-width="1.8" stroke-linejoin="round"><path d="M12 2l3 6.5 7 .8-5.2 4.8 1.5 7L12 17.6 5.7 21l1.5-7L2 9.3l7-.8z"/></svg>5</span></div></article>
    <article class="card"><div class="thumb"><div role="img" aria-label="Round dark keychain tracker holder" style="background:radial-gradient(circle at 60% 55%,#2e4258,#16202c 40%,#fff 46%)"></div></div><h3>Tagpod keychain</h3><p class="crumb">Gadgets &nbsp;›&nbsp; Other Gadgets</p>
      <div class="meta"><span><svg width="20" height="18" viewBox="0 0 24 22" fill="none" stroke="#222" stroke-width="1.8"><path d="M12 20S2 14 2 7.5A5 5 0 0112 5a5 5 0 0110 2.5C22 14 12 20 12 20z"/></svg>3,097</span><span><svg width="20" height="20" viewBox="0 0 24 24" fill="none" stroke="#222" stroke-width="1.8" stroke-linejoin="round"><path d="M12 2l3 6.5 7 .8-5.2 4.8 1.5 7L12 17.6 5.7 21l1.5-7L2 9.3l7-.8z"/></svg>5</span></div></article>
    <article class="card"><div class="thumb"><div role="img" aria-label="Black racing quadcopter drone" style="background:radial-gradient(ellipse,#3b3b3b,#1a1a1a 35%,#fff 50%)"></div></div><h3>FPV-Wing-Racer (rev.2)</h3><p class="crumb">Makers &nbsp;›&nbsp; RC &amp; Robotics</p>
      <div class="meta"><span><svg width="20" height="18" viewBox="0 0 24 22" fill="none" stroke="#222" stroke-width="1.8"><path d="M12 20S2 14 2 7.5A5 5 0 0112 5a5 5 0 0110 2.5C22 14 12 20 12 20z"/></svg>3,097</span><span><svg width="20" height="20" viewBox="0 0 24 24" fill="none" stroke="#222" stroke-width="1.8" stroke-linejoin="round"><path d="M12 2l3 6.5 7 .8-5.2 4.8 1.5 7L12 17.6 5.7 21l1.5-7L2 9.3l7-.8z"/></svg>5</span></div></article>
  </div>
</section>

<section>
  <div class="abs share">
    <div class="share-deco" role="img" aria-label="Bright yellow and pink decorative graphic"></div>
  </div>
  <div class="abs share-person" role="img" aria-label="Hooded fantasy character figure with long blonde hair"></div>
  <h2 class="abs display share-title">Have a Great Model to Share?</h2>
  <p class="abs share-text">Submit a file link to share with the community. We'll review and add it if it fits our curation standards.</p>
  <div class="abs btn share-btn">SUBMIT A FILE <svg width="20" height="12" viewBox="0 0 20 12" fill="none" stroke="#fff" stroke-width="1.8"><path d="M1 6h17M13 1l5 5-5 5"/></svg></div>
</section>

<section>
  <h2 class="abs section-title display" style="top:2658px">How MeshLocker Works</h2>
  <div class="abs steps">
    <div class="step"><div class="num" style="border-color:var(--pink)">01</div><h3>Search &amp; Filter</h3><p>Use powerful search &amp; smart filters to find STL files from multiple sources.</p></div>
    <div class="step"><div class="num" style="border-color:var(--orange)">02</div><h3>Explore Listings</h3><p>Browse clean, curated model previews with tags, categories, and source info.</p></div>
    <div class="step"><div class="num" style="border-color:var(--blue)">03</div><h3>Download &amp; Print</h3><p>Click "View on Source" to download directly from the original platform.</p></div>
  </div>
</section>

<footer class="abs footer">
  <div class="logo">Logo Here</div>
  <div class="social"><i></i><i></i></div>
  <div class="fcol" style="left:360px"><h4>Quick Links</h4><ul><li>Home</li><li>Categories</li><li>Popular</li><li>Submit a File</li><li>About</li><li>FAQ</li><li>Contact</li></ul></div>
  <div class="fcol" style="left:580px"><h4>Information</h4><ul><li>Shipping</li><li>Financing</li><li>Affiliate Program</li><li>Terms &amp; Conditions</li><li>Testimonials</li><li>Sitemap</li></ul></div>
  <div class="fcol" style="left:787px"><h4>Subscribe for Coupons, Tips &amp; Tricks</h4></div>
  <div class="email"><svg width="14" height="11" viewBox="0 0 14 11"><rect width="14" height="11" rx="1.5" fill="var(--orange)"/><path d="M1 1.5l6 4.5 6-4.5" fill="none" stroke="#111" stroke-width="1.2"/></svg>Enter email address</div>
  <div class="btn subscribe">SUBSCRIBE <svg width="16" height="16" viewBox="0 0 24 24" fill="#fff"><path d="M22 2L2 10l8 3 3 8z"/></svg></div>
  <div class="divider"></div>
  <p class="copy">© 2025 MeshLocker.net — Aggregating the 3D printing world</p>
  <svg class="chat" width="42" height="38" viewBox="0 0 42 38"><path d="M21 2C10 2 2 9 2 17c0 5 3 9 7 11l-2 8 9-6c2 .4 3 .5 5 .5 11 0 19-7 19-15S32 2 21 2z" fill="var(--orange)"/><circle cx="13" cy="17" r="2.5" fill="#111"/><circle cx="21" cy="17" r="2.5" fill="#111"/><circle cx="29" cy="17" r="2.5" fill="#111"/></svg>
</footer>

</body>
</html>
```